creating a certificate for our flagship course

Hi,
We need a new certificate for our flagship course called Rising Tide. We have been running this course for 25 years this year and want to get something special that represents that. We need our logos incorporated and we love to have a compass or Koru incorporated in the certificate. We like something different from your standard certificate, but not too crazy.

The text should say something along the lines of:
This certificate is awarded to ....
For successfully completing and contributing to the three day Rising Tide programme.

signed:... date:...

to learn a bit more about this course and our company, please check our website. www.veldonmarstik.co.nz

Thank you!

attendees who completed our 3 day programme.

• Both our RT logo and our brand logo. a compass or a koru.
• a 25th year existence something on it.

```html
<!DOCTYPE html>
<html lang="en">
<head>
<meta charset="utf-8">
<title>Rising Tide Certificate</title>
<link rel="stylesheet" href="https://fonts.googleapis.com/css2?family=Cabin:wght@400;500&display=swap">
<style>
  :root {
    --navy: #26243a;
    --navy-faint: #302e46;
    --paper: #ffffff;
    --paper-faint: #ebebeb;
    --green: #8bc756;
    --ink: #2a2838;
    --light: #f2f2f2;
  }
  * { margin: 0; padding: 0; box-sizing: border-box; }
  html, body { width: 1200px; height: 927px; overflow: hidden; background: var(--paper); }
  body { font-family: "Cabin", sans-serif; color: var(--ink); }

  .certificate { position: relative; width: 1200px; height: 927px; overflow: hidden; }
  .side-panel { position: absolute; left: 0; top: 0; width: 600px; height: 927px; background: var(--navy); }
  .emblem-backdrop { position: absolute; inset: 0; }

  .brand { position: absolute; left: 79px; top: 68px; display: flex; align-items: center; gap: 24px; }
  .brand-mark { width: 96px; height: 96px; background: var(--green); }
  .brand-name { color: var(--light); font-size: 38px; line-height: 1.05; font-weight: 500; letter-spacing: 1px; }

  .anniversary { position: absolute; left: 242px; top: 796px; width: 118px; text-align: center; color: var(--light); font-weight: 500; }
  .anniversary-number { display: block; font-size: 62px; line-height: 64px; }
  .anniversary-caption { display: block; font-size: 12px; letter-spacing: 0.5px; margin-top: 6px; }

  .title { position: absolute; left: 686px; top: 78px; font-size: 74px; font-weight: 400; color: var(--green); letter-spacing: 0.5px; }
  .awarded { position: absolute; left: 633px; width: 530px; top: 256px; text-align: center; font-size: 22px; letter-spacing: 3.5px; }
  .recipient-line { position: absolute; left: 633px; top: 367px; width: 530px; height: 1.5px; background: var(--green); }
  .citation { position: absolute; left: 633px; width: 530px; top: 485px; text-align: center; font-size: 32px; line-height: 50px; }

  .signatory { position: absolute; left: 800px; width: 200px; top: 707px; text-align: center; line-height: 1.1; }
  .signatory-name { font-size: 21px; }
  .signatory-role { font-size: 14px; }

  .programme { position: absolute; left: 688px; top: 847px; display: flex; align-items: center; gap: 6px; font-size: 11px; }
  .programme-mark { width: 24px; height: 24px; background: var(--green); }
  .date-field { position: absolute; left: 984px; top: 852px; font-size: 11px; }
</style>
</head>
<body>
<main class="certificate">
  <div class="side-panel"></div>

  <svg class="emblem-backdrop" width="1200" height="927" viewBox="0 0 1200 927" role="img" aria-label="Large faint emblem decoration">
    <defs>
      <clipPath id="left-half"><rect x="0" y="0" width="600" height="927"/></clipPath>
      <clipPath id="right-half"><rect x="600" y="0" width="600" height="927"/></clipPath>
    </defs>
    <circle cx="528" cy="500" r="275" fill="var(--navy-faint)" clip-path="url(#left-half)"/>
    <circle cx="528" cy="500" r="275" fill="var(--paper-faint)" clip-path="url(#right-half)"/>
  </svg>

  <div class="brand">
    <div class="brand-mark"></div>
    <div class="brand-name">VELDON<br>MARSTIK &amp; Associates</div>
  </div>

  <div class="anniversary">
    <span class="anniversary-number">25</span>
    <span class="anniversary-caption">YEARS WITH YOU</span>
  </div>

  <h1 class="title">CERTIFICATE</h1>
  <p class="awarded">awarded to:</p>
  <div class="recipient-line"></div>
  <p class="citation">For successfully completing and<br>contributing to the three day<br>Rising Tide programme.</p>

  <div class="signatory">
    <p class="signatory-name">Alan Brooke</p>
    <p class="signatory-role">MKT Manager</p>
  </div>

  <div class="programme">
    <div class="programme-mark"></div>
    <span>Rising Tide</span>
  </div>
  <p class="date-field">Month / Day / Year</p>
</main>
</body>
</html>
```